Flyer Design Project

We need a flyer (in Spanish) for:
"Feria Mezcal & Oficios Valle Dorado 2013"
This event will be held in Los Angeles CA and would like to attract exhibitors.
Must include the information provided in the word file.

Target Market(s)

Tequila producers and distributors

Industry/Entity Type

Event

Requirements
Must have
• pictures to be used at your discretion

```html
<!DOCTYPE html>
<html lang="es">
<head>
<meta charset="utf-8">
<title>Feria Mezcal &amp; Oficios Valle Dorado 2013</title>
<link rel="stylesheet" href="https://fonts.googleapis.com/css2?family=UnifrakturMaguntia&family=Pinyon+Script&family=Open+Sans:wght@600;700&display=swap">
<style>
  :root {
    --page: #ffffff;
    --parchment-light: #f3e8c9;
    --parchment-mid: #e6d3a4;
    --parchment-edge: #c9ac73;
    --wood-light: #b29878;
    --wood-dark: #6f5638;
    --ink: #111111;
    --field-green: #4f6a42;
    --field-sky: #a9c3d6;
    --cellar-brown: #6b4b2c;
    --cellar-light: #c9a37a;
    --clay-orange: #c86a2b;
    --clay-blue: #5a87b4;
    --crowd-warm: #8a5c3e;
    --crowd-light: #d9c3a8;
    --glass-gold: #e8d77a;
  }
  * { margin: 0; padding: 0; box-sizing: border-box; }
  html, body { width: 1200px; height: 1000px; overflow: hidden; background: var(--page); }
  .canvas { position: relative; width: 1200px; height: 1000px; }

  .flyer { position: absolute; left: 228px; top: 17px; width: 744px; height: 966px; }

  .photo-column { position: absolute; left: 0; top: 0; width: 314px; height: 966px; background: linear-gradient(90deg, var(--wood-light), #9c8263); }
  .photo { position: absolute; left: 0; width: 314px; }
  .photo-agave-field { top: 0; height: 201px; background: linear-gradient(180deg, var(--field-sky) 0%, #cfd8c9 22%, var(--field-green) 40%, #2f4533 100%); }
  .photo-barrel-cellar { top: 211px; height: 207px; background: linear-gradient(90deg, #efe9e2 0%, var(--cellar-light) 40%, var(--cellar-brown) 100%); }
  .photo-clay-pots { top: 430px; height: 268px; background: linear-gradient(120deg, var(--clay-orange) 0%, #9a4a1f 45%, #d78a45 65%, var(--clay-blue) 100%); }
  .photo-toast-friends { top: 708px; height: 258px; background: linear-gradient(180deg, var(--crowd-light) 0%, var(--crowd-warm) 55%, #3a2a22 100%); }

  .wood-divider { position: absolute; left: 312px; top: 0; width: 15px; height: 966px; background: linear-gradient(90deg, var(--wood-dark), var(--wood-light) 45%, var(--wood-dark)); }

  .text-panel {
    position: absolute; left: 327px; top: 0; width: 417px; height: 966px;
    background: radial-gradient(ellipse at 50% 45%, var(--parchment-light) 0%, var(--parchment-mid) 70%, var(--parchment-edge) 100%);
    color: var(--ink);
  }

  .event-title {
    position: absolute; left: 0; top: 34px; width: 100%;
    font-family: "UnifrakturMaguntia", serif; font-weight: 400;
    font-size: 37px; line-height: 42px; text-align: center;
  }
  .tagline {
    position: absolute; left: 8px; top: 152px; width: 401px;
    font-family: "Pinyon Script", cursive; font-size: 21px; line-height: 29px; text-align: center;
    white-space: nowrap;
  }

  .body-copy {
    position: absolute; left: 22px; width: 390px;
    font-family: "Open Sans", sans-serif; font-weight: 600; font-size: 13.2px; line-height: 19px;
    white-space: nowrap;
  }
  .copy-world { top: 230px; }
  .copy-promotion { top: 325px; }
  .copy-edition { top: 501px; }
  .copy-competition { top: 589px; }
  .copy-invite { top: 660px; }
  .copy-sponsor { top: 768px; left: 26px; font-size: 11.5px; font-weight: 700; }

  .contact {
    position: absolute; top: 813px; font-style: normal; white-space: nowrap;
    font-family: "Open Sans", sans-serif; font-weight: 600; font-size: 10.6px; line-height: 19px;
  }
  .contact-usa { left: 22px; }
  .contact-mexico { left: 242px; top: 809px; }

  .shot-glass { position: absolute; left: 182px; top: 829px; width: 42px; height: 56px; border-radius: 3px 3px 6px 6px;
    background: linear-gradient(180deg, #f8f4dc 0%, var(--glass-gold) 40%, #c9b255 100%); }

  .website {
    position: absolute; left: 0; top: 915px; width: 100%; text-align: center;
    font-family: "Open Sans", sans-serif; font-weight: 700; font-size: 21px; line-height: 29px;
  }
</style>
</head>
<body>
<div class="canvas">
  <div class="flyer">
    <div class="photo-column">
      <div class="photo photo-agave-field" role="img" aria-label="Campo de agave azul con un jimador trabajando bajo el cielo de montaña"></div>
      <div class="photo photo-barrel-cellar" role="img" aria-label="Dos maestros catando una copa junto a barricas de roble en la bodega"></div>
      <div class="photo photo-clay-pots" role="img" aria-label="Vasijas de barro artesanales naranjas con espirales negras"></div>
      <div class="photo photo-toast-friends" role="img" aria-label="Grupo de amigos sonrientes brindando con caballitos"></div>
    </div>
    <div class="wood-divider"></div>

    <section class="text-panel">
      <h1 class="event-title">Feria Mezcal &amp; Oficios<br>Valle Dorado 2013</h1>
      <p class="tagline">¡Vinculando marcas emergentes e innovadoras en una<br>época de descubrimiento de sabores mundiales!</p>

      <p class="body-copy copy-world">Chile, España, Escocia, Francia, Argentina, Polonia, Mexico<br>– cuando buscamos que beber, buscamos en el mundo, y ese<br>mundo termina en nuestros vasos. Queremos lo mejor, lo<br>más sabroso, lo interesante y estamos dispuestos a recorrer<br>grandes distancias para obtenerlo.</p>

      <p class="body-copy copy-promotion">&nbsp;La promoción y la creatividad son, quizás, aún más impor-<br>tante en tiempos de incertidumbre económica,<br>cuando se es implacable en la búsqueda de nuevos clientes.<br>Con unas perspectivas más amplias, más globales, ya sea<br>sondeando tradiciones centenarias, o la exploración de las<br>fronteras de las bebidas de moda, buscando nuevas merca-<br>dos, o re-inventando su marca para mantenerse competi-<br>tivos.</p>

      <p class="body-copy copy-edition">En esta edición especializada en Tequila, vamos a discutir las<br>técnicas, procesos creativos, perfiles de sabor, tecnologías, y<br>los ingredientes que son cada vez más esenciales de la caja<br>de herramientas del Coctelero (Mixologist) del siglo 21.</p>

      <p class="body-copy copy-competition">Tendremos una competencia de las cuatro variedades de<br>tequila: Blanco, Reposado, Añejo y Extra Añejo; con<br>reconocimiento a los ganadores de cada categoría.</p>

      <p class="body-copy copy-invite">Acompáñanos, los días 29 y 30 de agosto 2013, donde se<br>vincularan, consumidores, bares, detallistas, restaurantes y<br>distribuidores, en la matriz de creatividad coctelera, talento<br>culinario, sabores de moda&nbsp; y uno de los mercados más<br>importantes e influyentes&nbsp; del mundo.</p>

      <p class="body-copy copy-sponsor">Para oportunidades de patrocinio y exhibición:</p>

      <address class="contact contact-usa">
        (USA)<br>Ramiro L. Quintana – Director<br>Tel. + 818-555-0142<br>rquintana@ferivalle.com
      </address>
      <div class="shot-glass" role="img" aria-label="Caballito de tequila dorado"></div>
      <address class="contact contact-mexico">
        (Mexico)<br>Ing. Ernesto V. Lara<br>Tel. 333-555-0176<br>elara@ferivalle.com
      </address>

      <p class="website">www.ferivalle.com</p>
    </section>
  </div>
</div>
</body>
</html>
```